Business Card Design

We are a residential half way house for the addict ,the alcoholic and dual diagnosed in recovery.
i house both men and woman age 18+

Industry/Entity Type

Residential

```html
<!DOCTYPE html>
<html lang="en">
<head>
<meta charset="utf-8">
<title>Meridian Family Sober House – Business Card</title>
<link href="https://fonts.googleapis.com/css2?family=Tinos:wght@400;700&display=swap" rel="stylesheet">
<style>
  :root {
    --backdrop: #e6e3df;
    --card-black: #141414;
    --card-black-soft: #262626;
    --ink-white: #f4f4f4;
    --band-white: #f1f1f1;
    --accent-pink: #e0187a;
    --band-text: #1b1b1b;
  }
  html, body {
    margin: 0;
    width: 1200px;
    height: 892px;
    overflow: hidden;
    background: var(--backdrop);
  }
  .canvas {
    position: relative;
    width: 1200px;
    height: 892px;
  }
  .card {
    position: absolute;
    left: 75px;
    top: 146px;
    width: 1050px;
    height: 600px;
    overflow: hidden;
    background: linear-gradient(160deg, var(--card-black-soft) 0%, var(--card-black) 55%, #0c0c0c 100%);
    box-shadow: 0 18px 40px rgba(0,0,0,0.28);
    font-family: "Tinos", "Times New Roman", serif;
    color: var(--ink-white);
  }
  .company-name {
    position: absolute;
    left: 80px;
    top: 92px;
    margin: 0;
    font-weight: 400;
    font-size: 54px;
    line-height: 1.0;
    letter-spacing: 1px;
    text-transform: uppercase;
  }
  .company-name .line-two { display: block; padding-left: 62px; }
  .owner {
    position: absolute;
    left: 210px;
    top: 300px;
  }
  .owner-name {
    margin: 0;
    font-size: 34px;
    font-weight: 400;
    text-transform: uppercase;
    letter-spacing: 0.5px;
  }
  .owner-title {
    margin: 2px 0 0 0;
    font-size: 24px;
    text-transform: uppercase;
    display: inline-block;
    padding-bottom: 4px;
    border-bottom: 3px solid var(--accent-pink);
  }
  .tagline {
    margin: 6px 0 0 0;
    font-size: 22px;
  }
  .contact-list {
    position: absolute;
    right: 150px;
    top: 150px;
    margin: 0;
    padding: 0;
    list-style: none;
    text-align: right;
    font-size: 27px;
    line-height: 1.08;
  }
  .contact-list .email { margin-top: 18px; font-size: 24px; }
  .contact-rule {
    position: absolute;
    left: 926px;
    top: 0;
    width: 2px;
    height: 100%;
    background: var(--accent-pink);
  }
  .contact-icons {
    position: absolute;
    left: 911px;
    top: 42px;
    display: flex;
    flex-direction: column;
    gap: 10px;
  }
  .contact-icon {
    width: 32px;
    height: 32px;
    border-radius: 6px;
    background: var(--accent-pink);
    display: flex;
    align-items: center;
    justify-content: center;
  }
  .address-band {
    position: absolute;
    left: 0;
    top: 452px;
    width: 1050px;
    height: 58px;
    background: var(--band-white);
  }
  .address-band .pink-end {
    position: absolute;
    right: 0;
    top: 0;
    width: 124px;
    height: 100%;
    background: var(--accent-pink);
  }
  .address-band .pin {
    position: absolute;
    left: 940px;
    top: 15px;
  }
  .address-text {
    position: absolute;
    left: 215px;
    top: 0;
    margin: 0;
    line-height: 58px;
    font-size: 30px;
    color: var(--band-text);
  }
</style>
</head>
<body>
<div class="canvas">
  <section class="card" aria-label="Business card front">
    <h1 class="company-name">Meridian’s Family<span class="line-two">Sober House Inc.</span></h1>

    <div class="owner">
      <p class="owner-name">Dana Whitfield</p>
      <p class="owner-title">Owner</p>
      <p class="tagline">Your Sobriety is our Priority</p>
    </div>

    <div class="contact-rule"></div>
    <div class="contact-icons">
      <span class="contact-icon" aria-label="Phone">
        <svg width="18" height="18" viewBox="0 0 24 24"><path fill="#fff" d="M6.6 10.8a15.1 15.1 0 0 0 6.6 6.6l2.2-2.2c.3-.3.7-.4 1-.2 1.1.4 2.3.6 3.6.6.6 0 1 .4 1 1V20c0 .6-.4 1-1 1A17 17 0 0 1 3 4c0-.6.4-1 1-1h3.5c.6 0 1 .4 1 1 0 1.3.2 2.5.6 3.6.1.3 0 .7-.2 1z"/></svg>
      </span>
      <span class="contact-icon" aria-label="Phone">
        <svg width="18" height="18" viewBox="0 0 24 24"><path fill="#fff" d="M6.6 10.8a15.1 15.1 0 0 0 6.6 6.6l2.2-2.2c.3-.3.7-.4 1-.2 1.1.4 2.3.6 3.6.6.6 0 1 .4 1 1V20c0 .6-.4 1-1 1A17 17 0 0 1 3 4c0-.6.4-1 1-1h3.5c.6 0 1 .4 1 1 0 1.3.2 2.5.6 3.6.1.3 0 .7-.2 1z"/></svg>
      </span>
      <span class="contact-icon" aria-label="Fax">
        <svg width="18" height="18" viewBox="0 0 24 24"><rect x="6" y="3" width="12" height="6" fill="#fff"/><rect x="3" y="10" width="18" height="8" rx="1.5" fill="#fff"/><rect x="7" y="15" width="10" height="6" fill="#fff" stroke="#e0187a" stroke-width="1.5"/></svg>
      </span>
      <span class="contact-icon" aria-label="Email">
        <svg width="18" height="18" viewBox="0 0 24 24"><rect x="3" y="6" width="18" height="12" fill="#fff"/><path d="M3 6l9 7 9-7" fill="none" stroke="#e0187a" stroke-width="1.6"/></svg>
      </span>
    </div>

    <ul class="contact-list">
      <li>(555) 014-0305</li>
      <li>(555) 014-0306</li>
      <li>(555) 017-5536</li>
      <li class="email">danawhitfield@example.com</li>
    </ul>

    <div class="address-band">
      <div class="pink-end"></div>
      <svg class="pin" width="22" height="28" viewBox="0 0 24 30" aria-label="Location"><path fill="#fff" d="M12 1a9 9 0 0 0-9 9c0 7 9 18 9 18s9-11 9-18a9 9 0 0 0-9-9zm0 12.5a3.5 3.5 0 1 1 0-7 3.5 3.5 0 0 1 0 7z"/></svg>
      <p class="address-text">2750 Palm Grove Rd. Harbor Bend,Fla 33400</p>
    </div>
  </section>
</div>
</body>
</html>
```